New Website for novelty yarn producer

We need a new website for our company, Tarvek. We make highly tailored yarns for weavers worldwide. This year marks our 40th anniversary and we want to evolve our image and identity.

Our temporary website can be found at:
www.tarvekyarns.com

Our only concern in that throughout the website the protagonist must be our client, we make their creations possible and are highly adaptable both during the ideation process of the yarn as well as in the production. This is at the core of the way we do business and is summarised within the concept of FPM (Fluid Partner Method).

Industry/Entity Type

Textile

Number of Pages Required

1 page

Colors
9bcb3c

Requirements
Must have
• Fluid Partner Method (FPM) - can be found on or current website www.tarvekyarns.com

```html
<!DOCTYPE html>
<html lang="en">
<head>
<meta charset="utf-8">
<title>Tarvek Novelty Yarn Solutions</title>
<link href="https://fonts.googleapis.com/css2?family=Lato:wght@400;700;900&display=swap" rel="stylesheet">
<style>
:root{
  --green:#7cc22a;
  --green-bright:#c4ef4a;
  --green-pale:#eef8d8;
  --red:#f2195f;
  --teal:#4af0c2;
  --black:#000;
  --ink:#222;
  --text:#4a4a4a;
  --muted:#777;
  --section-grey:#f6f6f6;
  --white:#fff;
}
*{margin:0;padding:0;box-sizing:border-box}
html,body{width:1200px;height:2889px;overflow:hidden}
body{position:relative;background:var(--white);font-family:'Lato',sans-serif;color:var(--text)}
.abs{position:absolute}

/* header */
.site-header{left:0;top:0;width:1200px;height:116px;background:var(--black)}
.brand{left:112px;top:28px;color:var(--white);font-weight:900;font-size:40px;letter-spacing:1px;display:flex;align-items:center;gap:12px}
.brand-dot{width:14px;height:14px;background:var(--green);border-radius:50%}
.main-nav{top:46px;color:var(--white);font-size:19px;font-weight:700}
.main-nav span{position:absolute;top:0;white-space:nowrap}

/* hero */
.hero{left:0;top:116px;width:1200px;height:608px;background:radial-gradient(ellipse at 50% 45%,#6b5a4a 0%,#3d3129 45%,#1c1612 100%)}
.hero-mark{left:448px;top:258px;display:flex;align-items:center;gap:22px;color:var(--white)}
.hero-mark .ring{width:74px;height:74px;border:3px solid var(--green);border-radius:50%}
.hero-mark .label{border-left:2px solid rgba(255,255,255,.7);padding-left:20px;font-size:26px;line-height:30px;text-transform:uppercase;font-weight:400}

/* intro */
.intro{left:0;top:724px;width:1200px;height:505px;overflow:hidden}
.intro-title{top:90px;width:1200px;text-align:center;font-size:56px;font-weight:900;color:var(--black);letter-spacing:-.5px}
.intro-title em{font-style:normal;color:var(--green)}
.intro-sub{top:240px;width:1200px;text-align:center;font-size:30px;font-weight:700;color:var(--black)}
.intro-sub em{font-style:normal;color:var(--green)}
.intro-copy{top:318px;left:100px;width:1000px;text-align:center;font-size:18px;line-height:24px;color:var(--text)}

/* steps */
.steps{left:0;top:1229px;width:1200px;height:1208px;background:var(--section-grey)}
.step-title{font-size:60px;font-weight:900;color:var(--green);letter-spacing:-.5px;white-space:nowrap}
.step-copy{font-size:23px;line-height:27px;color:var(--text);letter-spacing:.3px;white-space:nowrap}
.right{text-align:right}

/* footer */
.site-footer{left:0;top:2437px;width:1200px;height:381px;background:var(--white)}
.foot-head{top:75px;font-size:19px;font-weight:700;color:var(--ink)}
.foot-rule{top:100px;height:3px;background:var(--green)}
.foot-small{font-size:12.5px;line-height:21px;color:var(--muted)}
.foot-small b{color:var(--ink)}
.quick-links li{list-style:none;position:relative;padding-left:26px;font-size:13px;line-height:32px;color:var(--muted)}
.quick-links li::before{content:"";position:absolute;left:0;top:11px;border-left:8px solid var(--green);border-top:5px solid transparent;border-bottom:5px solid transparent}
.social{width:44px;height:44px;border:2px solid var(--ink);border-radius:50%}
.newsletter-input{left:905px;top:2634px;width:182px;height:34px;border-radius:17px;background:#eee;font-size:13px;color:var(--ink);padding:9px 16px}
.to-top{left:1111px;top:2750px;width:54px;height:54px;border-radius:50%;background:var(--green)}
.bottom-bar{left:0;top:2818px;width:1200px;height:71px;background:var(--black);color:var(--white);font-size:13px;text-align:center;line-height:71px;letter-spacing:.5px}
</style>
</head>
<body>

<header class="site-header abs">
  <div class="brand abs">TARVEK<span class="brand-dot"></span></div>
  <nav class="main-nav abs">
    <span style="left:710px">HOME</span>
    <span style="left:808px">ABOUT US</span>
    <span style="left:942px">FPM</span>
    <span style="left:1035px">MORE</span>
  </nav>
</header>

<section class="hero abs" role="img" aria-label="Close-up photograph of yarn spinning machinery in the mill">
  <div class="hero-mark abs">
    <div class="ring"></div>
    <div class="label">Fluid<br>Partner<br>Method</div>
  </div>
</section>

<section class="intro abs">
  <svg class="abs" style="left:0;top:0" width="1200" height="505" aria-hidden="true">
    <circle cx="40" cy="80" r="150" fill="none" stroke="var(--green-pale)" stroke-width="6"/>
    <circle cx="1180" cy="290" r="150" fill="none" stroke="var(--green-pale)" stroke-width="6"/>
  </svg>
  <h1 class="intro-title abs"><em>Flexible</em> at the core</h1>
  <h2 class="intro-sub abs"><em>TVK</em> Fluid Partner Method</h2>
  <p class="intro-copy abs">We believe that the key to delivering a yarn that exceeds our client's expectation is to work together<br>with weavers from step one, starting from the desired end product and working backwards. This allows us<br>to develop the product that our weavers need, rather than having weavers adapt to the supplied<br>raw materials. Our Fluid Partner Method consists achieving maximum flexibility both in<br>development and production.</p>
</section>

<section class="steps abs">
  <svg class="abs" style="left:0;top:0" width="1200" height="1208" aria-hidden="true">
    <path d="M 745 325 A 135 135 0 1 1 953 325" fill="none" stroke="var(--red)" stroke-width="8" stroke-linecap="round"/>
    <circle cx="849" cy="366" r="19" fill="var(--red)"/>
    <g fill="none" stroke="#333" stroke-width="4" stroke-linecap="round" stroke-linejoin="round">
      <path d="M829 274 a34 34 0 1 1 40 0 v22 h-40 z"/>
      <path d="M833 308 h32 M837 318 h24"/>
      <path d="M840 262 l9 -10 l9 10"/>
      <path d="M800 208 l10 8 M898 208 l-10 8 M849 186 v12 M788 240 h12 M898 240 h12"/>
    </g>
    <path d="M 246 620 A 130 130 0 1 1 351 711" fill="none" stroke="var(--green-bright)" stroke-width="8" stroke-linecap="round"/>
    <circle cx="233" cy="651" r="19" fill="var(--green-bright)"/>
    <g fill="none" stroke="#333" stroke-width="4" stroke-linejoin="round">
      <rect x="292" y="542" width="112" height="96" rx="6"/>
      <rect x="328" y="528" width="40" height="18"/>
      <circle cx="348" cy="590" r="14"/>
      <path d="M348 546 v30 M348 604 v20 M318 624 h60"/>
      <rect x="306" y="620" width="24" height="14"/>
      <rect x="366" y="620" width="24" height="14"/>
    </g>
    <path d="M 955 903 A 130 130 0 1 1 890 848" fill="none" stroke="var(--teal)" stroke-width="8" stroke-linecap="round"/>
    <circle cx="973" cy="876" r="19" fill="var(--teal)"/>
    <g fill="none" stroke="#333" stroke-width="4" stroke-linejoin="round">
      <path d="M792 1020 v-50 l30 -18 v18 l30 -18 v18 l30 -18 v68 z"/>
      <rect x="856" y="910" width="14" height="60"/>
      <rect x="880" y="898" width="14" height="72"/>
      <rect x="840" y="986" width="44" height="26"/>
      <path d="M862 986 v26 M840 999 h44 M780 1020 h140"/>
    </g>
  </svg>

  <h2 class="step-title abs" style="left:112px;top:90px">IDEATION</h2>
  <p class="step-copy abs" style="left:116px;top:223px">We define goals and parameters<br>meeting with all the players, designers,<br>technicians, sales force and logisitcs.<br>We analyse together all aspects and factors:<br>strategy, technology, raw materiales<br>and markets in order to define our GOALs.</p>

  <h2 class="step-title abs right" style="left:600px;top:443px;width:488px">EXECUTION</h2>
  <p class="step-copy abs right" style="left:500px;top:582px;width:588px">Once the goals are defined, our FPM team<br>starts straging internal meetings and<br>working with technicians, technical partners,<br>yarn and raw material suppliers, and produce<br>the first prototype for testing and analysing.</p>

  <h2 class="step-title abs" style="left:112px;top:800px">SCALING PRODUCTION</h2>
  <p class="step-copy abs" style="left:112px;top:952px">When the novelty yarn is defined, the<br>process of scaling up starts. Putting the<br>value-added products into production at<br>an industrial scale, making sure through<br>continuous tuning that the most efficient<br>and successful process are adopted.</p>
</section>

<footer class="site-footer abs">
  <h3 class="foot-head abs" style="left:112px">Tarvek Novelty Yarn Solutions</h3>
  <div class="foot-rule abs" style="left:112px;width:240px"></div>
  <p class="foot-small abs" style="left:112px;top:138px;width:280px"><b>Tarvek s.r.l</b><br>Via dei Filatori 12 - 50100 Borgo Lana - Italy<br>Tel. 0555 01234 r.a.<br>Fax 0555 01299<br>R.E.A BL 480211<br>Reg. Imp. BL 04417320915<br><b>P. IVA 00428100553</b><br>Cod. Fisc. 04417320915<br>Capitale sociale € 50. 000, 00 int. ver.</p>

  <h3 class="foot-head abs" style="left:412px">Quick Links</h3>
  <div class="foot-rule abs" style="left:412px;width:130px"></div>
  <ul class="quick-links abs" style="left:412px;top:130px">
    <li>Home</li><li>About us</li><li>FPM</li><li>Heritage</li><li>Team</li><li>Blog</li><li>Contact</li>
  </ul>

  <h3 class="foot-head abs" style="left:657px">Follow Us</h3>
  <div class="foot-rule abs" style="left:657px;width:128px"></div>
  <div class="social abs" style="left:657px;top:141px"></div>
  <div class="social abs" style="left:725px;top:141px"></div>
  <div class="social abs" style="left:657px;top:212px"></div>
  <div class="social abs" style="left:725px;top:212px"></div>

  <h3 class="foot-head abs" style="left:907px">Newsletter</h3>
  <div class="foot-rule abs" style="left:907px;width:130px"></div>
  <p class="foot-small abs" style="left:905px;top:136px;width:200px">At vero eos et accusamus et dignissimos ducimus .</p>
</footer>
<div class="newsletter-input abs">Your Email Address</div>
<div class="to-top abs">
  <svg width="54" height="54" aria-hidden="true"><path d="M16 32 L27 21 L38 32" fill="none" stroke="var(--white)" stroke-width="5" stroke-linecap="round" stroke-linejoin="round"/></svg>
</div>
<div class="bottom-bar abs">© TARVEK COPYRIGHT 2018. ALL RIGHTS RESERVED.</div>

</body>
</html>
```